Modern Innovative Business Card Design

We require a nice, modern, clean business card design, ready for upload to Cardomora. Our company develops online banking software solutions for small financial insitutions. The design should be clean, professional, but yet not "corporate boring". See www.fyrolt.com for an idea of business image and profile. The design should communicate innovation, be modern and fresh, yet look professional and established.

Target Market(s)

Finance industry, bankers, entrepreneurs

Industry/Entity Type

Financial

Contact Information for Business Card

Tobias Wendlerup
CEO

FYROLT BV
Lindenwerf 38
1027 HX Amsterdam
The Netherlands

Phone: +31 20 517 8036
Direct: +31 20 604 1758
Callory: tobias.fyrolt
ceo@fyrolt.com
www.fyrolt.com

Font styles to use
Sans Serif

Requirements
Must have
• Should look clean, modern and professional. File should be ready for upload to cardomora.
Should not have
• Boring standard corporate layout

```html
<!DOCTYPE html>
<html lang="en">
<head>
<meta charset="utf-8">
<title>FYROLT Business Card</title>
<link href="https://fonts.googleapis.com/css2?family=Ubuntu+Condensed&display=swap" rel="stylesheet">
<style>
  :root {
    --green: #8dc63f;
    --green-faint: #b3da7f;
    --white: #ffffff;
    --ink: #4d4d4d;
    --stage: #e9e9e6;
    --card-shadow: 0 6px 18px rgba(0,0,0,0.18);
  }
  * { margin: 0; padding: 0; box-sizing: border-box; }
  html, body {
    width: 1200px; height: 960px; overflow: hidden;
    background: var(--stage);
    font-family: "Ubuntu Condensed", "Arial Narrow", sans-serif;
  }
  .canvas { position: relative; width: 1200px; height: 960px; }

  .card { position: absolute; width: 640px; height: 390px; overflow: hidden; box-shadow: var(--card-shadow); }

  /* Front */
  .card-front { left: 90px; top: 70px; background: var(--green); }
  .front-faint {
    position: absolute; left: -10px; color: var(--green-faint);
    font-size: 190px; line-height: 1; letter-spacing: 6px; white-space: nowrap;
  }
  .front-faint.top { top: -40px; }
  .front-faint.bottom { top: 250px; left: -60px; }
  .front-name {
    position: absolute; left: 0; right: 0; top: 145px; text-align: center;
    color: var(--white); font-size: 104px; line-height: 1; letter-spacing: 8px;
  }

  /* Back */
  .card-back { left: 490px; top: 500px; background: var(--white); }
  .back-band { position: absolute; inset: 0; }
  .holder { position: absolute; left: 42px; top: 46px; color: var(--green); white-space: nowrap; }
  .holder-name { font-size: 34px; line-height: 1; }
  .holder-title { font-size: 26px; line-height: 1.1; margin-top: 4px; }

  .contact {
    position: absolute; color: var(--ink); font-size: 18px; line-height: 22px;
    display: flex; gap: 8px; text-transform: uppercase; white-space: nowrap;
  }
  .contact svg { flex: none; margin-top: 2px; }
  .contact-address { left: 42px; top: 130px; width: 280px; }
  .contact-phone { left: 335px; top: 130px; }
  .contact-chat { left: 42px; top: 218px; width: 280px; }
  .contact-mail { left: 335px; top: 218px; }
  .contact-web { left: 42px; top: 266px; }

  .back-name {
    position: absolute; left: 352px; top: 292px; color: var(--ink);
    font-size: 52px; line-height: 1; letter-spacing: 5px; white-space: nowrap;
  }
</style>
</head>
<body>
<div class="canvas">

  <section class="card card-front" aria-label="Card front">
    <div class="front-faint top" aria-hidden="true">FYROLT</div>
    <div class="front-faint bottom" aria-hidden="true">FYROLT</div>
    <div class="front-name">FYROLT</div>
  </section>

  <section class="card card-back" aria-label="Card back">
    <svg class="back-band" width="640" height="390" viewBox="0 0 640 390" aria-hidden="true">
      <path d="M0 298 C 220 285, 450 260, 640 200 L 640 282 C 450 345, 220 372, 0 384 Z" fill="var(--green)"/>
    </svg>

    <div class="holder">
      <div class="holder-name">TOBIAS WENDLERUP</div>
      <div class="holder-title">CEO FYROLT</div>
    </div>

    <div class="contact contact-address">
      <svg width="16" height="24" viewBox="0 0 16 24"><path d="M8 0a8 8 0 0 0-8 8c0 6 8 16 8 16s8-10 8-16a8 8 0 0 0-8-8z" fill="var(--green)"/><circle cx="8" cy="8" r="3" fill="var(--white)"/></svg>
      <div>FYROLT BV Lindenwerf 38<br>1027 HX Amsterdam<br>The Netherlands</div>
    </div>

    <div class="contact contact-phone">
      <svg width="18" height="18" viewBox="0 0 24 24"><path d="M6.6 10.8a15 15 0 0 0 6.6 6.6l2.2-2.2c.3-.3.7-.4 1-.2 1.1.4 2.3.6 3.6.6.6 0 1 .4 1 1V20c0 .6-.4 1-1 1A17 17 0 0 1 3 4c0-.6.4-1 1-1h3.5c.6 0 1 .4 1 1 0 1.3.2 2.5.6 3.6.1.3 0 .7-.2 1z" fill="var(--green)"/></svg>
      <div>Phone: +31 20 517 8036<br>Direct: +31 20 604 1758</div>
    </div>

    <div class="contact contact-chat">
      <svg width="18" height="18" viewBox="0 0 18 18"><circle cx="9" cy="9" r="9" fill="var(--green)"/></svg>
      <div>Callory: tobias.fyrolt</div>
    </div>

    <div class="contact contact-mail">
      <svg width="20" height="14" viewBox="0 0 20 14"><rect width="20" height="14" fill="var(--green)"/><path d="M0 0l10 8 10-8" fill="none" stroke="var(--white)" stroke-width="1.6"/></svg>
      <div>ceo@fyrolt.com</div>
    </div>

    <div class="contact contact-web">
      <svg width="18" height="18" viewBox="0 0 20 20"><g fill="none" stroke="var(--green)" stroke-width="1.6"><circle cx="10" cy="10" r="8.5"/><ellipse cx="10" cy="10" rx="3.8" ry="8.5"/><path d="M1.5 10h17M3 5.5h14M3 14.5h14"/></g></svg>
      <div>www.fyrolt.com</div>
    </div>

    <div class="back-name">FYROLT</div>
  </section>

</div>
</body>
</html>
```